Brochure design for Velicor

Create a bi-fold A5 size brochure. I have attached our logo and the written content to be included in the brochure. So the brochure will have a total of 4 pages (front page, inner two pages, back page). End source files need to include final printable brochure as well as editable files.

```html
<!DOCTYPE html>
<html lang="en">
<head>
<meta charset="utf-8">
<title>Velicor brochure – back and front cover</title>
<link rel="stylesheet" href="https://fonts.googleapis.com/css2?family=Baloo+2:wght@600;700&family=Lato:wght@400;700&display=swap">
<style>
  :root{
    --bg:#6f6f6f;
    --paper:#ffffff;
    --brand-blue:#1c6aae;
    --brand-teal:#1f8f8a;
    --brand-green:#7cc243;
    --text-dark:#2d2d2d;
    --text-grey:#6a6a6a;
  }
  *{margin:0;padding:0;box-sizing:border-box}
  html,body{width:1200px;height:1200px;overflow:hidden;background:var(--bg)}
  .spread{position:absolute;left:120px;top:260px;width:960px;height:679px;display:flex;box-shadow:0 10px 30px rgba(0,0,0,.3)}
  .page{position:relative;width:480px;height:679px;background:var(--paper);overflow:hidden}
  .page svg.page-art{position:absolute;inset:0;width:100%;height:100%}

  /* back page */
  .references{position:absolute;left:46px;top:86px;width:392px;list-style:none;font-family:"Lato",sans-serif;font-size:8.2px;line-height:1.38;color:var(--text-dark)}
  .references li{position:relative;padding-left:26px;margin-bottom:6px}
  .references li::before{content:attr(data-n);position:absolute;left:0;top:0;width:13px;height:13px;border-radius:50%;background:var(--brand-teal);color:#fff;font-size:7px;font-weight:700;text-align:center;line-height:13px}
  .fee-note{position:absolute;left:72px;top:472px;font-family:"Lato",sans-serif;font-size:8px;color:var(--brand-blue)}
  .contact{position:absolute;left:262px;top:466px;font-family:"Lato",sans-serif;font-size:11px;letter-spacing:1.5px;color:var(--text-grey)}
  .contact p{display:flex;align-items:center;gap:9px;margin-bottom:8px}
  .contact svg{width:13px;height:13px}
  .brand{font-family:"Baloo 2",sans-serif;font-weight:700;color:var(--brand-blue);line-height:1;display:flex;align-items:center;gap:7px}
  .brand .dot{width:12px;height:12px;border-radius:50%;background:var(--brand-green)}
  .brand-tag{font-family:"Lato",sans-serif;font-size:8px;font-weight:700;color:var(--brand-green);margin-top:2px;padding-left:19px}
  .back-brand{position:absolute;left:120px;top:530px}
  .back-brand .brand{font-size:34px}

  /* front page */
  .front-brand{position:absolute;left:0;right:0;top:38px;display:flex;flex-direction:column;align-items:center}
  .front-brand .brand{font-size:34px}
  .headline{position:absolute;left:110px;right:20px;top:412px;text-align:center;font-family:"Baloo 2",sans-serif;font-weight:700;font-size:26px;line-height:1.12}
  .headline .soft{color:var(--text-grey);font-weight:600}
  .headline .strong{color:var(--brand-green)}
  .front-rule{position:absolute;left:130px;right:40px;top:600px;height:1px;background:#cfcfcf}
  .front-web{position:absolute;left:110px;right:20px;top:612px;text-align:center;font-family:"Lato",sans-serif;font-size:10px;letter-spacing:5px;color:var(--text-grey)}
</style>
</head>
<body>
<main class="spread">
  <!-- Back page -->
  <section class="page page-back">
    <svg class="page-art" viewBox="0 0 480 679" aria-hidden="true">
      <defs>
        <linearGradient id="arcBack" x1="0" y1="1" x2="1" y2="0">
          <stop offset="0" stop-color="#7cc243"/><stop offset="1" stop-color="#1c6aae"/>
        </linearGradient>
        <linearGradient id="fadeBack" x1="0" y1="0" x2="0" y2="1">
          <stop offset="0" stop-color="#ffffff" stop-opacity="0"/><stop offset="1" stop-color="#dff0ee"/>
        </linearGradient>
      </defs>
      <path d="M0,170 C10,110 50,70 110,50" fill="none" stroke="url(#arcBack)" stroke-width="4"/>
      <path d="M0,190 C14,126 58,84 118,62" fill="none" stroke="#7cc243" stroke-width="1.5" opacity=".6"/>
    </svg>
    <svg class="page-art" viewBox="0 0 480 679" role="img" aria-label="Faint DNA helix image fading into the lower page">
      <rect x="0" y="560" width="480" height="119" fill="url(#fadeBack)"/>
    </svg>
    <ol class="references">
      <li data-n="1">2003 Release: International Consortium Completes HGP. Available at: https://www.humangenomeinfo.org/2003-release-international-consortium-completes-hgp/</li>
      <li data-n="2">Marlow KT, Dessen-Pryce A, Holt R: Clinical application of pharmacogenetics. Trends Mol. Med.7, 201-204 (2001).</li>
      <li data-n="3">Brandt H, et al. Pharmacogenetics 1998;8:283-289.</li>
      <li data-n="4">Lio K, et al. Journal of Molecular Diagnostics 2016;18(3):438-45.</li>
      <li data-n="5">Carver DL, et al. Clinical Pharmacology and Therapeutics 2016;100(2):160-9.</li>
      <li data-n="6">Farrani P, et al. Pharmacogenomics and Personalized Medicine 2017;27(10):17-27.</li>
      <li data-n="7">Osterhout JM, et al. Clinical Pharmacology and Therapeutics 2014;95(4):423-31.</li>
      <li data-n="8">R. Whitcombe, et al. Food elimination based on IgG antibodies in irritable bowel syndrome: a randomised controlled trial. Gut 53 (2004):1459-1464. DOI: 10.1136/gut.2003.037697.</li>
      <li data-n="9">Helena Marsh et al. Randomised controlled trial of food elimination diet based IgG antibodies for the prevention of migraine like headaches. Nutrition Journal 10 (2011):85. DOI:10.1186/1475-2891-10-85.</li>
      <li data-n="10">Alvarado Ruiz CP, Echeverri Soto M, Fuentes Morel HL. Food allergy mediated by IgG antibodies associated with migraine in adults. Revista Alergia México 54 (2007):162-8.</li>
      <li data-n="11">D. Corvani, L. Franceschi, P. Amato. Immune complexes in food-induced arthralgia. Ann Allergy 59 (1987):422-8.</li>
    </ol>
    <p class="fee-note">* Additional fees may apply.</p>
    <div class="contact">
      <p><svg viewBox="0 0 14 14"><rect x="1" y="3" width="12" height="8" rx="1" fill="none" stroke="#1c6aae" stroke-width="1.4"/><path d="M1.5,3.5 7,8 12.5,3.5" fill="none" stroke="#1c6aae" stroke-width="1.4"/></svg>enquiries@velicor.co</p>
      <p><svg viewBox="0 0 14 14"><circle cx="7" cy="7" r="5.8" fill="none" stroke="#1c6aae" stroke-width="1.3"/><ellipse cx="7" cy="7" rx="2.5" ry="5.8" fill="none" stroke="#1c6aae" stroke-width="1"/><path d="M1.2,7H12.8M2.2,4H11.8M2.2,10H11.8" stroke="#1c6aae" stroke-width="1"/></svg>www.velicor.co</p>
    </div>
    <div class="back-brand">
      <div class="brand"><span class="dot"></span>velicor</div>
      <div class="brand-tag">Personalised Health &amp; Wellness</div>
    </div>
  </section>

  <!-- Front page -->
  <section class="page page-front">
    <svg class="page-art" viewBox="0 0 480 679">
      <defs>
        <linearGradient id="photoTone" x1="0" y1="0" x2="1" y2="0.6">
          <stop offset="0" stop-color="#ffffff"/>
          <stop offset=".35" stop-color="#e3edf4"/>
          <stop offset=".8" stop-color="#a9c9e2"/>
          <stop offset="1" stop-color="#7fb0d6"/>
        </linearGradient>
        <linearGradient id="bandTone" x1="0" y1="1" x2="1" y2="0">
          <stop offset="0" stop-color="#7cc243"/><stop offset=".55" stop-color="#1f8f8a"/><stop offset="1" stop-color="#7cc243"/>
        </linearGradient>
        <linearGradient id="lowerTone" x1="0" y1="0" x2="0" y2="1">
          <stop offset="0" stop-color="#f4f5f6"/><stop offset="1" stop-color="#e6e8ea"/>
        </linearGradient>
      </defs>
      <rect width="480" height="679" fill="url(#lowerTone)"/>
      <path role="img" aria-label="Photograph of a gloved hand holding a glowing molecular model on a soft blue laboratory background"
            d="M0,0 H480 V352 C400,368 300,378 200,394 C100,414 20,464 0,580 Z" fill="url(#photoTone)"/>
      <path d="M0,580 C20,464 100,414 200,394 C300,378 400,368 480,352" fill="none" stroke="url(#bandTone)" stroke-width="5"/>
      <path d="M20,679 C40,610 90,585 170,578 C280,570 400,562 480,550" fill="none" stroke="#7cc243" stroke-width="2.5"/>
    </svg>
    <div class="front-brand">
      <div class="brand"><span class="dot"></span>velicor</div>
      <div class="brand-tag">Personalised Health &amp; Wellness</div>
    </div>
    <h1 class="headline">
      <span class="soft">A revolution in</span><br>
      <span class="strong">HEALTH &amp; WELLNESS</span><br>
      <span class="soft">has been brewing</span><br>
      <span class="strong">AND NOW IT IS HERE!</span>
    </h1>
    <div class="front-rule"></div>
    <p class="front-web">www.velicor.co</p>
  </section>
</main>
</body>
</html>
```